Forensic investigators looking for updated powerpoint design

Louisiana company called Bayline Analytics has an important upcoming meeting and needs a redesigned slideshow template. They are an engineering firm providing evaluation, reporting, and expert witness testimony on a variety of topics to support the litigation and insurance industries. The meeting in question will be held at a conference catering to insurance underwriters.

Target Market(s)

Upcoming tradeshow presentation

Industry/Entity Type

Insurance; TIC (Testing, Inspection, Certification)

Font styles to use
Sans Serif

Colors
0054AA
0677BA
7BADD7
CADEEF
E8F1F8
FFC000
F8CF3A
FAE287
FDF2CF
FEFAEE

Requirements
Must have
• Updated background template with examples of different layouts (bullet list w/ graphic, bullet list without, quote, large central photo, etc.), implementing company logo
Nice to have
• Visual motif that carries through powerpoint designs
Should not have
• No hexagons (old motif of parent company that we're moving away from)

```html
<!DOCTYPE html>
<html lang="en">
<head>
<meta charset="utf-8">
<title>Bayline Analytics – Slide Template</title>
<link rel="stylesheet" href="https://fonts.googleapis.com/css2?family=Exo:wght@600;700&family=Poppins:wght@400;500;600&display=swap">
<style>
  :root {
    --blue: #0054AA;
    --blue-mid: #0677BA;
    --blue-soft: #7BADD7;
    --blue-pale: #CADEEF;
    --blue-mist: #E8F1F8;
    --yellow: #FFC000;
    --yellow-warm: #F8CF3A;
    --ink: #111111;
    --grey: #9a9a9a;
    --stage: #3a3a3a;
    --white: #ffffff;
  }
  * { box-sizing: border-box; margin: 0; padding: 0; }
  html, body { width: 1200px; height: 1090px; overflow: hidden; background: var(--stage); }
  body { position: relative; font-family: "Poppins", Arial, sans-serif; color: var(--ink); }

  .slide { position: absolute; width: 483px; height: 271px; background: var(--white); overflow: hidden; }
  .slide--cover   { left: 100px; top: 98px; }
  .slide--outline { left: 618px; top: 98px; }
  .slide--stat    { left: 100px; top: 410px; }
  .slide--quote   { left: 618px; top: 410px; }
  .slide--decay   { left: 100px; top: 720px; }
  .slide--photo   { left: 618px; top: 720px; }

  .slide__bar { position: absolute; left: 0; bottom: 0; width: 100%; height: 7px; background: var(--blue); }

  .slide__title { position: absolute; left: 26px; top: 19px; font-family: "Exo", Arial, sans-serif; font-weight: 700; font-size: 24px; line-height: 22px; letter-spacing: 0.2px; }
  .slide__title .accent { color: var(--yellow); display: block; }
  .slide__title .main { color: var(--blue); display: block; }

  .slide__text { position: absolute; left: 26px; width: 434px; font-size: 8.1px; line-height: 11px; font-weight: 500; }
  .justify { text-align: justify; }

  .footer__url { position: absolute; left: 26px; bottom: 12px; font-size: 6px; font-weight: 600; display: flex; align-items: center; gap: 2px; }
  .footer__url svg { width: 6px; height: 6px; }
  .brand { position: absolute; display: flex; align-items: center; gap: 3px; color: var(--blue); font-family: "Exo", Arial, sans-serif; font-weight: 700; white-space: nowrap; }
  .brand__mark { background: var(--ink); display: block; }
  .brand--footer { right: 20px; bottom: 13px; font-size: 9.5px; }
  .brand--footer .brand__mark { width: 12px; height: 12px; }

  .photo { position: absolute; }

  /* cover */
  .brand--cover { left: 24px; top: 25px; font-size: 20px; gap: 4px; }
  .brand--cover .brand__mark { width: 24px; height: 24px; }
  .cover__headline { position: absolute; left: 24px; top: 159px; font-family: "Exo", Arial, sans-serif; font-weight: 700; font-size: 23px; line-height: 22px; letter-spacing: 0.3px; }
  .cover__headline .y { color: var(--yellow); display: block; }
  .cover__headline .k { color: var(--ink); display: block; }
  .cover__headline .b { color: var(--blue); display: block; }
  .cover__sub { position: absolute; left: 24px; top: 229px; font-size: 8.2px; line-height: 10px; font-weight: 500; width: 250px; }
  .cover__art { position: absolute; inset: 0; }

  /* outline */
  .outline__list { position: absolute; left: 26px; top: 77px; list-style: none; font-size: 8.4px; font-weight: 500; }
  .outline__list li { height: 15px; display: flex; align-items: center; gap: 4px; }
  .outline__list svg { width: 6px; height: 6px; flex: none; }

  /* quote */
  .quote__sub { position: absolute; left: 26px; top: 102px; color: var(--yellow); font-size: 10px; line-height: 11px; font-weight: 500; }
  .quote__body { position: absolute; left: 26px; top: 137px; width: 233px; font-size: 8.3px; line-height: 9.6px; font-weight: 500; text-align: justify; }
  .quote__cite { position: absolute; left: 26px; top: 204px; width: 233px; font-size: 6.5px; line-height: 9.6px; color: var(--grey); text-align: justify; }
  .stat__source { position: absolute; left: 26px; top: 97px; font-size: 7px; color: var(--grey); }
</style>
</head>
<body>

<!-- Cover -->
<section class="slide slide--cover">
  <svg class="cover__art" viewBox="0 0 483 271" role="img" aria-label="Photo of a yellow hard hat, level, tape measure and hands sketching on architectural blueprints">
    <defs>
      <linearGradient id="coverPhoto" x1="0.2" y1="0" x2="0.9" y2="1">
        <stop offset="0" stop-color="#f6c81a"/>
        <stop offset="0.28" stop-color="#f3dc7a"/>
        <stop offset="0.5" stop-color="#ecebe8"/>
        <stop offset="0.75" stop-color="#e3ddd6"/>
        <stop offset="1" stop-color="#d8b59a"/>
      </linearGradient>
    </defs>
    <polygon points="238,0 483,0 483,271 310,271" fill="url(#coverPhoto)"/>
    <line x1="226" y1="0" x2="297" y2="271" stroke="#FFC000" stroke-width="3"/>
    <line x1="234" y1="0" x2="305" y2="271" stroke="#0054AA" stroke-width="3"/>
  </svg>
  <div class="brand brand--cover"><span class="brand__mark"></span>Bayline Analytics</div>
  <h1 class="cover__headline">
    <span class="y">BAYLINE ANALYTICS</span>
    <span class="k">A CONSULTING</span>
    <span class="b">ENGINEERING FIRM.</span>
  </h1>
  <p class="cover__sub">Joined The Bayline Analytics Team as the Client Services Manager for North Carolina, South Carolina, and Virginia.</p>
</section>

<!-- Course outline -->
<section class="slide slide--outline">
  <svg class="photo" style="left:0;top:0" width="483" height="271" viewBox="0 0 483 271" role="img" aria-label="Photo of blueprints with drafting tools, magnifier, calculator and a yellow hard hat">
    <defs>
      <linearGradient id="outlinePhoto" x1="0" y1="0.3" x2="1" y2="0.5">
        <stop offset="0" stop-color="#f4f4f4"/>
        <stop offset="0.55" stop-color="#e2e2e2"/>
        <stop offset="0.85" stop-color="#f2d250"/>
        <stop offset="1" stop-color="#f6c40c"/>
      </linearGradient>
    </defs>
    <polygon points="171,0 483,0 483,118 385,216" fill="url(#outlinePhoto)"/>
  </svg>
  <h2 class="slide__title"><span class="accent">Course</span><span class="main">Outline</span></h2>
  <ul class="outline__list">
    <li><svg viewBox="0 0 10 10"><circle cx="5" cy="5" r="4.2" fill="none" stroke="#FFC000" stroke-width="1.3"/><path d="M3 5.2l1.5 1.5L7.2 3.8" fill="none" stroke="#FFC000" stroke-width="1.3"/></svg>Purpose</li>
    <li><svg viewBox="0 0 10 10"><circle cx="5" cy="5" r="4.2" fill="none" stroke="#FFC000" stroke-width="1.3"/><path d="M3 5.2l1.5 1.5L7.2 3.8" fill="none" stroke="#FFC000" stroke-width="1.3"/></svg>Wood decay - "Biodeterioration"</li>
    <li><svg viewBox="0 0 10 10"><circle cx="5" cy="5" r="4.2" fill="none" stroke="#FFC000" stroke-width="1.3"/><path d="M3 5.2l1.5 1.5L7.2 3.8" fill="none" stroke="#FFC000" stroke-width="1.3"/></svg>How long does it take for a piece of wood to decay?</li>
    <li><svg viewBox="0 0 10 10"><circle cx="5" cy="5" r="4.2" fill="none" stroke="#FFC000" stroke-width="1.3"/><path d="M3 5.2l1.5 1.5L7.2 3.8" fill="none" stroke="#FFC000" stroke-width="1.3"/></svg>Mold, Decay and Fungus</li>
    <li><svg viewBox="0 0 10 10"><circle cx="5" cy="5" r="4.2" fill="none" stroke="#FFC000" stroke-width="1.3"/><path d="M3 5.2l1.5 1.5L7.2 3.8" fill="none" stroke="#FFC000" stroke-width="1.3"/></svg>Types of decay</li>
    <li><svg viewBox="0 0 10 10"><circle cx="5" cy="5" r="4.2" fill="none" stroke="#FFC000" stroke-width="1.3"/><path d="M3 5.2l1.5 1.5L7.2 3.8" fill="none" stroke="#FFC000" stroke-width="1.3"/></svg>Necessary Ingredients and Optimum Conditions</li>
    <li><svg viewBox="0 0 10 10"><circle cx="5" cy="5" r="4.2" fill="none" stroke="#FFC000" stroke-width="1.3"/><path d="M3 5.2l1.5 1.5L7.2 3.8" fill="none" stroke="#FFC000" stroke-width="1.3"/></svg>Sources of Moisture</li>
    <li><svg viewBox="0 0 10 10"><circle cx="5" cy="5" r="4.2" fill="none" stroke="#FFC000" stroke-width="1.3"/><path d="M3 5.2l1.5 1.5L7.2 3.8" fill="none" stroke="#FFC000" stroke-width="1.3"/></svg>Important Points</li>
    <li><svg viewBox="0 0 10 10"><circle cx="5" cy="5" r="4.2" fill="none" stroke="#FFC000" stroke-width="1.3"/><path d="M3 5.2l1.5 1.5L7.2 3.8" fill="none" stroke="#FFC000" stroke-width="1.3"/></svg>Results of Moisture Exposure Tests</li>
  </ul>
  <div class="footer__url"><svg viewBox="0 0 10 10"><circle cx="5" cy="5" r="4" fill="none" stroke="#0054AA"/><path d="M1 5h8M5 1c-2 2.5-2 5.5 0 8M5 1c2 2.5 2 5.5 0 8" fill="none" stroke="#0054AA" stroke-width=".7"/></svg>www.baylineanalytics.com</div>
  <div class="brand brand--footer"><span class="brand__mark"></span>Bayline Analytics</div>
  <div class="slide__bar"></div>
</section>

<!-- Statistic -->
<section class="slide slide--stat">
  <h2 class="slide__title"><span class="accent">Interesting</span><span class="main">Statistic</span></h2>
  <p class="slide__text justify" style="top:75px">Current estimates show that replacement materials, needed to repair damage caused by rot alone, account for nearly 10 percent of U.S. annual wood production.</p>
  <p class="stat__source">(Midstate University Extension)</p>
  <div class="photo" style="left:26px;top:115px;width:434px;height:107px;background:linear-gradient(90deg,#8a6a4c 0%,#d6bf95 18%,#9c6e42 34%,#e2cda4 52%,#b27a44 70%,#c99a62 85%,#8e5b30 100%);" role="img" aria-label="Photo of stacked lumber bundles in a warehouse"></div>
  <div class="footer__url"><svg viewBox="0 0 10 10"><circle cx="5" cy="5" r="4" fill="none" stroke="#0054AA"/><path d="M1 5h8M5 1c-2 2.5-2 5.5 0 8M5 1c2 2.5 2 5.5 0 8" fill="none" stroke="#0054AA" stroke-width=".7"/></svg>www.baylineanalytics.com</div>
  <div class="brand brand--footer"><span class="brand__mark"></span>Bayline Analytics</div>
  <div class="slide__bar"></div>
</section>

<!-- Quote -->
<section class="slide slide--quote">
  <svg class="photo" style="left:0;top:0" width="483" height="271" viewBox="0 0 483 271" role="img" aria-label="Photo of metal gears and a pen resting on engineering drawings">
    <defs>
      <linearGradient id="quotePhoto" x1="0" y1="0" x2="1" y2="1">
        <stop offset="0" stop-color="#dfe7f1"/>
        <stop offset="0.35" stop-color="#8d96a3"/>
        <stop offset="0.55" stop-color="#c3ccd8"/>
        <stop offset="0.75" stop-color="#2f7fb0"/>
        <stop offset="1" stop-color="#e7edf4"/>
      </linearGradient>
    </defs>
    <polygon points="168,0 483,0 483,118 385,216" fill="url(#quotePhoto)"/>
  </svg>
  <h2 class="slide__title"><span class="accent">Wood</span><span class="main">Decay (Rot)</span></h2>
  <p class="quote__sub">How long does it Take<br>for a Piece of Wood to Decay?</p>
  <p class="quote__body">"There is no way even to crudely estimate the rate of wood decay or its age. Wood decay is a complex biological phenomenon subject to many physical and environmental factors, such as moisture level, temperature, wood species, fungus species, geographic locality, and climate"</p>
  <p class="quote__cite">Dana R. Holloway, Biological Technician with the National Timber Research Laboratory Reference: Rot Never Sleeps All it takes is some wood and a little moisture - By Martin Crane, July 12, 1999.</p>
  <div class="footer__url"><svg viewBox="0 0 10 10"><circle cx="5" cy="5" r="4" fill="none" stroke="#0054AA"/><path d="M1 5h8M5 1c-2 2.5-2 5.5 0 8M5 1c2 2.5 2 5.5 0 8" fill="none" stroke="#0054AA" stroke-width=".7"/></svg>www.baylineanalytics.com</div>
  <div class="brand brand--footer"><span class="brand__mark"></span>Bayline Analytics</div>
  <div class="slide__bar"></div>
</section>

<!-- Decay -->
<section class="slide slide--decay">
  <h2 class="slide__title"><span class="accent">Decay</span></h2>
  <p class="slide__text" style="top:51px">Decay fungus may appear as fan-shaped patches, strands, or root-like structures that are usually white or brown in color.</p>
  <p class="slide__text" style="top:84px">Sometimes fruiting bodies are produced that take the form of mushrooms, brackets, or crusts. The fungus, in the form of microscopic, threadlike strands called hyphae, permeates the wood and uses parts of it as food.</p>
  <div class="photo" style="left:26px;top:127px;width:434px;height:107px;background:linear-gradient(165deg,#b06a3e 0%,#c9c9cf 22%,#e3ddd2 40%,#c9ab8c 60%,#b57a4e 80%,#9a5f38 100%);" role="img" aria-label="Photo of fungal decay growing on wood beneath a window frame"></div>
  <div class="footer__url"><svg viewBox="0 0 10 10"><circle cx="5" cy="5" r="4" fill="none" stroke="#0054AA"/><path d="M1 5h8M5 1c-2 2.5-2 5.5 0 8M5 1c2 2.5 2 5.5 0 8" fill="none" stroke="#0054AA" stroke-width=".7"/></svg>www.baylineanalytics.com</div>
  <div class="brand brand--footer"><span class="brand__mark"></span>Bayline Analytics</div>
  <div class="slide__bar"></div>
</section>

<!-- Large photo -->
<section class="slide slide--photo">
  <h2 class="slide__title"><span class="accent">Heading</span><span class="main">Goes Here</span></h2>
  <div class="photo" style="left:24px;top:82px;width:434px;height:148px;background:linear-gradient(180deg,#7fb0de 0%,#b5cfe6 22%,#c9c8c3 38%,#a9a59c 55%,#b9ab93 70%,#cbbda4 100%);" role="img" aria-label="Photo of a concrete block house under construction on a dirt lot"></div>
  <div class="footer__url"><svg viewBox="0 0 10 10"><circle cx="5" cy="5" r="4" fill="none" stroke="#0054AA"/><path d="M1 5h8M5 1c-2 2.5-2 5.5 0 8M5 1c2 2.5 2 5.5 0 8" fill="none" stroke="#0054AA" stroke-width=".7"/></svg>www.baylineanalytics.com</div>
  <div class="brand brand--footer"><span class="brand__mark"></span>Bayline Analytics</div>
  <div class="slide__bar"></div>
</section>

</body>
</html>
```